Butcher shop

We have 2 butcher shops:

Shop 7, Ridgeway Court, Aberdeen NSW 2336
Ph 02 6519 4482

58 Partridge St, Scone NSW 2337
Ph 02 6538 2170

ABN 47 308 915 226

I would like this info on reverse of card and my personal info on front of card. I have a logo I would like to use also. Require a very smooth thick matte card, with colour both sides.

Front of card should say:

Lorna Tewsbury
Accounts

Ph 0427 615 903
E lornatewsbury@mailnest.example

Industry/Entity Type

Shop

Contact Information for Business Card

Lorna Tewsbury
Ph 0427 615 903

Logo Text

Tewsbury's Quality Meats

Logo styles of interest
Pictorial/Combination Logo
Requirements
Must have
• We use Century Gothic Font

```html
<!DOCTYPE html>
<html lang="en">
<head>
<meta charset="utf-8">
<title>Tewsbury's Quality Meats — Business Card</title>
<link rel="stylesheet" href="https://fonts.googleapis.com/css2?family=Questrial&family=Open+Sans:wght@700&display=swap">
<style>
  :root {
    --stage: #2b2b2b;
    --stage-edge: #161616;
    --sky: #8fd6f1;
    --ink: #0b0d12;
    --black: #050505;
    --navy: #1b2c4d;
    --navy-deep: #0d1628;
    --white: #ffffff;
  }
  * { box-sizing: border-box; margin: 0; padding: 0; }
  html, body { width: 1200px; height: 1200px; overflow: hidden; }
  body {
    background: radial-gradient(circle at 50% 40%, var(--stage) 0%, var(--stage-edge) 100%);
    font-family: "Questrial", "Century Gothic", sans-serif;
    position: relative;
  }
  .card {
    position: absolute;
    left: 120px;
    width: 960px;
    height: 549px;
    overflow: hidden;
    box-shadow: 0 18px 40px rgba(0,0,0,0.55);
  }
  /* Front */
  .card--front { top: 36px; background: var(--sky); }
  .front__top-band {
    position: absolute; left: 0; top: 0; width: 100%; height: 56px;
    background: var(--black);
  }
  .front__bottom-band {
    position: absolute; left: 0; bottom: 0; width: 100%; height: 92px;
    background: linear-gradient(180deg, var(--navy) 0%, var(--navy-deep) 100%);
  }
  .brand {
    position: absolute;
    display: flex; align-items: center; gap: 22px;
  }
  .brand__mark { width: 34px; height: 34px; flex: none; }
  .brand__name {
    font-size: 42px; line-height: 1.08; letter-spacing: 0.5px; white-space: nowrap;
  }
  .card--front .brand { left: 110px; top: 222px; }
  .card--front .brand__mark { background: var(--ink); }
  .card--front .brand__name { color: var(--ink); }
  .front__divider {
    position: absolute; left: 470px; top: 180px; width: 2px; height: 180px;
    background: var(--ink);
  }
  .contact {
    position: absolute; left: 520px; top: 168px; color: var(--ink);
  }
  .contact__name { font-size: 32px; line-height: 1.15; white-space: nowrap; }
  .contact__role { font-size: 32px; line-height: 1.15; padding-left: 28px; }
  .contact__lines { margin-top: 34px; padding-left: 70px; font-size: 21px; line-height: 1.35; white-space: nowrap; }
  /* Back */
  .card--back {
    top: 615px;
    background: linear-gradient(160deg, var(--black) 0%, var(--black) 45%, var(--navy) 100%);
  }
  .card--back .brand { left: 80px; top: 250px; }
  .card--back .brand__mark { background: var(--sky); }
  .card--back .brand__name { color: var(--sky); font-size: 50px; }
  .abn {
    position: absolute; left: 130px; top: 400px;
    font-family: "Open Sans", sans-serif; font-weight: 700;
    font-size: 26px; color: var(--white); letter-spacing: 0.5px; white-space: nowrap;
  }
  .shop {
    position: absolute; width: 380px; height: 210px;
  }
  .shop__shape { position: absolute; inset: 0; width: 100%; height: 100%; }
  .shop__text {
    position: absolute; left: 122px; top: 104px;
    font-family: "Open Sans", sans-serif; font-weight: 700;
    font-size: 19px; line-height: 1.25; color: var(--ink); white-space: nowrap;
  }
  .shop--kelvale { left: 470px; top: 34px; }
  .shop--brookhurst { left: 560px; top: 266px; }
</style>
</head>
<body>
  <section class="card card--front" aria-label="Card front">
    <div class="front__top-band"></div>
    <div class="brand">
      <span class="brand__mark"></span>
      <span class="brand__name">Tewsbury's<br>Quality Meats</span>
    </div>
    <div class="front__divider"></div>
    <div class="contact">
      <p class="contact__name">Lorna Tewsbury</p>
      <p class="contact__role">Accounts</p>
      <div class="contact__lines">
        <p>Ph 0427 615 903</p>
        <p>E lornatewsbury@mailnest.example</p>
      </div>
    </div>
    <div class="front__bottom-band"></div>
  </section>

  <section class="card card--back" aria-label="Card back">
    <div class="brand">
      <span class="brand__mark"></span>
      <span class="brand__name">Tewsbury's<br>Quality Meats</span>
    </div>
    <p class="abn">ABN 47 308 915 226</p>

    <div class="shop shop--kelvale">
      <svg class="shop__shape" viewBox="0 0 380 210" aria-hidden="true">
        <polygon points="110,210 110,105 0,105 190,0 380,105 380,210" fill="#8fd6f1"/>
      </svg>
      <p class="shop__text">58 Partridge St,<br>Kelvale NSW 2361<br>Ph 02 6538 2170</p>
    </div>

    <div class="shop shop--brookhurst">
      <svg class="shop__shape" viewBox="0 0 380 210" aria-hidden="true">
        <polygon points="110,210 110,105 0,105 190,0 380,105 380,210" fill="#8fd6f1"/>
      </svg>
      <p class="shop__text">Shop 7, Ridgeway Court,<br>Brookhurst NSW 2354<br>Ph 02 6519 4482</p>
    </div>
  </section>
</body>
</html>
```